Preoperative Medical clearance for Patients on blood thinners

Prepare a flow chart which directs medical office staff to properly triage patients preparing for surgery who are on blood thinners. We will provide a rudimentary flow chart with all necessary information. We need a better layout which is more appealing and intuitive.

Target Market(s)

internal office use

Industry/Entity Type

Medical

Font styles to use
Sans Serif

Requirements
Must have
• attractive, intuitive layout
Should not have
• things that promote confusion

```html
<!DOCTYPE html>
<html lang="en">
<head>
<meta charset="utf-8">
<title>Preoperative Clearance – Patients on Blood Thinners</title>
<link href="https://fonts.googleapis.com/css2?family=Kalam:wght@700&family=Montserrat:wght@500;600;700&display=swap" rel="stylesheet">
<style>
  :root{
    --red:#e60000;
    --red-mid:#b30000;
    --red-deep:#8e0000;
    --red-fold:#5c0000;
    --green-bar:#009a00;
    --green-head:#00c800;
    --green-box:#009300;
    --green-fold:#0b4a0b;
    --orange:#f55600;
    --blue:#0a7bd1;
    --yellow:#ffff00;
    --ink:#111;
    --white:#fff;
  }
  html,body{margin:0;padding:0;overflow:hidden;}
  body{width:1080px;height:1200px;position:relative;font-family:'Montserrat',sans-serif;background:#777;}
  .hero-photo{position:absolute;left:0;top:0;width:1080px;height:468px;
    background:linear-gradient(90deg,#c9ced3 0%,#d8dde1 45%,#b9c3cc 62%,#3a64b0 75%,#2c55a6 100%);}
  .ward-photo{position:absolute;left:0;top:468px;width:1080px;height:732px;
    background:linear-gradient(180deg,#9a9a9a 0%,#6f6f6f 45%,#8a8a8a 75%,#a8a8a8 100%);}
  .title{position:absolute;left:68px;top:82px;margin:0;font-family:'Kalam',cursive;font-weight:700;
    color:var(--red);font-size:72px;line-height:80px;letter-spacing:1px;}
  .decision-bar{position:absolute;left:25px;top:306px;width:907px;height:53px;background:var(--green-bar);
    color:var(--white);font-weight:700;font-size:32px;display:flex;align-items:center;justify-content:center;}
  .decision-no{position:absolute;left:932px;top:306px;width:86px;height:53px;background:var(--red);
    color:var(--white);font-weight:500;font-size:24px;display:flex;align-items:center;justify-content:center;}
  .question-band{position:absolute;left:20px;top:468px;width:1038px;height:74px;background:var(--yellow);
    color:var(--ink);font-weight:600;font-size:34px;display:flex;align-items:center;justify-content:center;}
  .shapes{position:absolute;left:0;top:0;}
  .cell{position:absolute;box-sizing:border-box;display:flex;align-items:center;justify-content:center;
    text-align:center;color:var(--white);font-weight:600;line-height:1.2;padding:0 8px;}
  .category{background:var(--orange);font-size:24px;font-weight:700;letter-spacing:1px;}
  .ask{background:var(--blue);font-size:21px;font-weight:600;}
  .ask-small{background:var(--blue);font-size:14px;}
  .yes-head{background:var(--green-head);font-size:20px;font-weight:700;}
  .no-head{background:var(--red);font-size:20px;font-weight:700;}
  .step-green{background:var(--green-box);font-size:15px;}
  .step-red{background:var(--red);font-size:14px;}
  .step-mid{background:var(--red-mid);}
  .step-deep{background:var(--red-deep);}
  .small{font-size:13.5px;}
</style>
</head>
<body>
  <div class="hero-photo" role="img" aria-label="Photo of a surgeon in blue scrubs with arms crossed in a hospital room"></div>
  <div class="ward-photo" role="img" aria-label="Blurred grayscale photo of a hospital ward"></div>

  <h1 class="title">Patient taking a<br>blood thinner?</h1>

  <svg class="shapes" width="1080" height="1200" viewBox="0 0 1080 1200" aria-hidden="true">
    <polygon points="80,359 980,359 522,412" fill="var(--yellow)"/>
    <polygon points="1018,306 1050,333 1018,359" fill="var(--red)"/>
    <!-- cardiac folds -->
    <polygon points="42,870 182,870 42,906" fill="var(--green-fold)"/>
    <polygon points="206,1034 345,1034 345,1092" fill="var(--red-fold)"/>
    <!-- neurologist -->
    <polygon points="385,832 523,832 385,870" fill="var(--green-fold)"/>
    <polygon points="548,889 617,889 523,940 385,940" fill="var(--green-fold)"/>
    <rect x="617" y="889" width="70" height="29" fill="var(--red-fold)"/>
    <polygon points="548,918 687,918 617,889" fill="var(--red-fold)"/>
    <polygon points="385,1124 523,1124 385,1160" fill="var(--green-fold)"/>
    <polygon points="548,1010 687,1010 687,1046" fill="var(--red-fold)"/>
    <!-- hematologist -->
    <polygon points="730,832 870,832 730,868" fill="var(--green-fold)"/>
    <polygon points="894,889 963,889 874,942 734,942" fill="var(--green-fold)"/>
    <rect x="963" y="889" width="71" height="29" fill="var(--red-fold)"/>
    <polygon points="894,918 1034,918 963,889" fill="var(--red-fold)"/>
    <polygon points="734,1118 874,1118 734,1154" fill="var(--green-fold)"/>
    <polygon points="894,1003 1034,1003 1034,1040" fill="var(--red-fold)"/>
  </svg>

  <div class="decision-bar">YES</div>
  <div class="decision-no">NO?</div>
  <div class="question-band">Cardiac problem, bleeding disorder, or stroke?</div>

  <!-- Cardiac -->
  <div class="cell category" style="left:42px;top:579px;width:303px;height:59px;">CARDIAC</div>
  <div class="cell ask" style="left:42px;top:638px;width:303px;height:58px;">Have a cardiologist?</div>
  <div class="cell yes-head" style="left:42px;top:696px;width:140px;height:58px;">YES</div>
  <div class="cell step-green" style="left:42px;top:754px;width:140px;height:116px;">Refer to Patient’s current cardiologist</div>
  <div class="cell no-head" style="left:206px;top:696px;width:139px;height:58px;">NO</div>
  <div class="cell step-red" style="left:206px;top:754px;width:139px;height:96px;font-size:17px;">Have a primary care doctor?</div>
  <div class="cell step-red step-mid small" style="left:206px;top:850px;width:139px;height:92px;">Call primary and ask for preffered cardiologist.</div>
  <div class="cell step-red step-deep" style="left:206px;top:942px;width:139px;height:92px;font-size:14.5px;">Refer to cardiologist selected by primary</div>

  <!-- Stroke / bleeding disorder -->
  <div class="cell category" style="left:385px;top:579px;width:649px;height:59px;">STROKE / BLEEDING DISORDER</div>

  <div class="cell ask" style="left:385px;top:638px;width:302px;height:58px;">Have a neurologist?</div>
  <div class="cell yes-head" style="left:385px;top:696px;width:138px;height:58px;">YES</div>
  <div class="cell step-green" style="left:385px;top:754px;width:138px;height:78px;">Refer to patient’s neurologist</div>
  <div class="cell no-head" style="left:548px;top:696px;width:139px;height:58px;">NO</div>
  <div class="cell ask-small" style="left:548px;top:754px;width:139px;height:78px;">Have primary care doctor?</div>
  <div class="cell yes-head" style="left:548px;top:832px;width:69px;height:57px;font-size:17px;padding:0;">YES</div>
  <div class="cell no-head" style="left:617px;top:832px;width:70px;height:57px;font-size:17px;padding:0;">NO</div>
  <div class="cell step-green small" style="left:385px;top:940px;width:138px;height:92px;">Call primary and ask for preffered cardiologist.</div>
  <div class="cell step-green" style="left:385px;top:1032px;width:138px;height:92px;">Refer to cardiologist selected by primary</div>
  <div class="cell step-red small" style="left:548px;top:918px;width:139px;height:92px;">Selet specialist and refer to establish care</div>

  <div class="cell ask" style="left:730px;top:638px;width:304px;height:58px;">Have a hematologist?</div>
  <div class="cell yes-head" style="left:730px;top:696px;width:140px;height:58px;">YES</div>
  <div class="cell step-green" style="left:730px;top:754px;width:140px;height:78px;">Refer to hematologist for clearance</div>
  <div class="cell no-head" style="left:894px;top:696px;width:140px;height:58px;">NO</div>
  <div class="cell ask-small" style="left:894px;top:754px;width:140px;height:68px;">Have primary care doctor?</div>
  <div class="cell yes-head" style="left:894px;top:822px;width:69px;height:67px;font-size:17px;padding:0;">YES</div>
  <div class="cell no-head" style="left:963px;top:822px;width:71px;height:67px;font-size:17px;padding:0;">NO</div>
  <div class="cell step-green small" style="left:734px;top:942px;width:140px;height:88px;">Call primary and ask for preffered cardiologist.</div>
  <div class="cell step-green" style="left:734px;top:1030px;width:140px;height:88px;">Refer to cardiologist selected by primary</div>
  <div class="cell step-red small" style="left:894px;top:918px;width:140px;height:85px;">Selet specialist and refer to establish care</div>
</body>
</html>
```